Business Card for new Overseas Property Buying Business

Hi

We need a new business card for our new business.

We are Faraway Nest Finders. So we search locations on behalf of our clients to find them the ideal home.

These are mainly holiday homes in nice locations - but sometimes people are looking to relocate.

I am looking for a nice simple design - that has some class and professionalism about it. Taking inspiration from our logo.

Text wise I was thinking of maybe having something like. (THE FONT FOR THIS SHOULD BE LIKE THE WRITING IN THE ATTACHMENT WITH THE MAP ON IT)

1)
What does your dream house have (tick all that apply):
swimming pool x
private vineyard x
herb garden x
full sized football pitch x

2)
How to buy a home abroad:

Method 1:
1) Scour internet for suitable estate agents
2) Arrange hectic holiday timetable with multiple agents in multiple languages
3) Fly to destination to find property was not as it seemed
4) Feel frustrated and helpless
OR
Method 2:
Contact your expert home hunter (details overleaf) - and leave the hard work to them

The end result should give people confidence that they are dealing with a professional organisation - and feel like they can place their trust in them. I would want it to drive them to either contact us directly or visit the website.

Please include name (Gordon Tramley), position (founder), contact numbers x 2, email address, website (www.quelvatrix-moor.com)

I look forward to seeing your entries.

Reason: Hi Sorry to extend - Xmas has got in the way of my plans. I will be providing feedback. Happy Christmas to you all.

```html
<!DOCTYPE html>
<html lang="en">
<head>
<meta charset="utf-8">
<title>Larkfield &amp; Orne – Business Card</title>
<link rel="stylesheet" href="https://fonts.googleapis.com/css2?family=Nothing+You+Could+Do&family=Old+Standard+TT:wght@700&display=swap">
<style>
  :root{
    --page:#f1f1f1;
    --ink:#3c2f25;
    --ink-soft:#4d4a48;
    --accent:#e0602f;
    --parchment-light:#f0d496;
    --parchment-dark:#d7a65c;
    --paper-light:#f3f2ef;
    --paper-dark:#dedcd7;
    --rule:#6e6a66;
  }
  *{box-sizing:border-box;margin:0;padding:0}
  html,body{width:1200px;height:874px;overflow:hidden;background:var(--page)}
  .canvas{position:relative;width:1200px;height:874px}
  .hand{font-family:"Nothing You Could Do",cursive}
  .serif{font-family:"Old Standard TT",serif;font-weight:700}

  .brand-lockup{position:absolute;left:40px;top:60px;width:300px;text-align:center;color:var(--ink)}
  .brand-lockup .mark{width:120px;height:120px;border-radius:50%;background:var(--accent);margin:0 auto 22px}
  .brand-lockup .name{font-size:40px;line-height:1}
  .brand-lockup .tagline{font-size:15px;letter-spacing:1.5px;margin-top:6px;text-transform:uppercase}

  .card{position:absolute;box-shadow:0 6px 18px rgba(0,0,0,.18)}
  .card-front{left:600px;top:50px;width:560px;height:320px}
  .card-back{left:60px;top:470px;width:640px;height:364px}
  .card-surface{position:absolute;inset:0}
  .front-surface{background:radial-gradient(ellipse at 40% 40%,var(--parchment-light),var(--parchment-dark))}
  .back-surface{background:linear-gradient(160deg,var(--paper-light),var(--paper-dark))}

  .front-brand{position:absolute;left:24px;top:24px;width:230px;color:var(--ink)}
  .front-brand .name{font-size:26px;line-height:1;white-space:nowrap}
  .front-brand .tagline{font-size:10px;letter-spacing:1.1px;text-transform:uppercase;margin-top:4px;white-space:nowrap}
  .front-mark{position:absolute;left:60px;top:130px;width:100px;height:100px;border-radius:50%;background:var(--accent)}
  .contact{position:absolute;left:272px;top:60px;width:270px;list-style:none;color:var(--ink);font-size:20px;line-height:1.6;white-space:nowrap}
  .contact .name{padding-left:70px}
  .contact .role{padding-left:120px}
  .contact .phone{padding-left:100px}

  .back-body{position:absolute;inset:22px 24px;display:flex;color:var(--ink-soft)}
  .back-col{flex:1;font-size:15px;line-height:1.3}
  .divider{width:2px;background:var(--rule);margin:0 16px;opacity:.8}
  .wishlist h2,.howto h2{font:inherit;font-size:17px}
  .wishlist .hint{margin-bottom:18px}
  .wishlist ul{list-style:none;text-align:right;padding-right:8px;font-size:17px;line-height:1.7}
  .howto ol{list-style:none}
  .howto .method{margin-top:2px}
  .back-brand{color:var(--ink);margin-top:4px;line-height:1}
  .back-brand .name{font-size:17px}
  .back-brand .tagline{font-size:7px;letter-spacing:.8px;text-transform:uppercase}
</style>
</head>
<body>
<main class="canvas">

  <section class="brand-lockup" aria-label="Brand lockup">
    <div class="mark"></div>
    <div class="name serif">Larkfield&amp;Orne</div>
    <div class="tagline serif">Faraway Nest Finders</div>
  </section>

  <article class="card card-front">
    <div class="card-surface front-surface" role="img" aria-label="Antique parchment world map background"></div>
    <div class="front-brand">
      <div class="name serif">Larkfield&amp;Orne</div>
      <div class="tagline serif">Faraway Nest Finders</div>
    </div>
    <div class="front-mark"></div>
    <ul class="contact hand">
      <li class="name">Gordon Tramley</li>
      <li class="role">founder</li>
      <li class="phone">555.010.2841</li>
      <li class="phone">555.010.2842</li>
      <li>gordon@quelvatrix-moor.com</li>
      <li>www.quelvatrix-moor.com</li>
    </ul>
  </article>

  <article class="card card-back">
    <div class="card-surface back-surface" role="img" aria-label="Faint grey world map on postcard paper"></div>
    <div class="back-body hand">
      <section class="back-col wishlist">
        <h2>What does your dream house have?</h2>
        <p class="hint">(tick all that apply)</p>
        <ul>
          <li>swimming pool x</li>
          <li>private vineyard x</li>
          <li>herb garden x</li>
          <li>full sized football pitch x</li>
        </ul>
      </section>
      <div class="divider"></div>
      <section class="back-col howto">
        <h2>How to buy a home abroad</h2>
        <p class="method">Method 1:</p>
        <ol>
          <li>1) Scour internet for suitable estate agents</li>
          <li>2) Arrange hectic holiday timetable with multiple agents in multiple languages</li>
          <li>3) Fly to destination to find property was not as it seemed</li>
          <li>4) Feel frustrated and helpless</li>
        </ol>
        <p>OR</p>
        <p class="method">Method 2:</p>
        <p>Contact your expert home hunter</p>
        <div class="back-brand">
          <div class="name serif">Larkfield&amp;Orne</div>
          <div class="tagline serif">Faraway Nest Finders</div>
        </div>
        <p>– and leave the hard work to them!</p>
      </section>
    </div>
  </article>

</main>
</body>
</html>
```